terras letterhead

We would like to create a new letterhead that our company will use for proposals, invoices, statements and letters. Our company name is Terra-Vantage. We are a landscape design/build and landscape maintenance company. We have a web site Terra-Vantage.example where our logo (the leaf with the lettering within it only) is displayed.

Industry/Entity Type

Graphic Design

Requirements
Must have
• Address and info on our current letterhead (uploaded)
Nice to have
• We would like the design to look presentable in grey scale as well as color.
Should not have
• Do not want to infringe much on the normal useable area within the normal print areas.

```html
<!DOCTYPE html>
<html lang="en">
<head>
<meta charset="utf-8">
<title>Terra-Vantage Letterhead</title>
<link rel="stylesheet" href="https://fonts.googleapis.com/css2?family=Arimo:wght@400;700&display=swap">
<style>
  :root {
    --backdrop: #e6e6e3;
    --paper: #ffffff;
    --forest: #1d3a0a;
    --ink: #111111;
  }
  html, body {
    margin: 0;
    padding: 0;
    width: 848px;
    height: 1200px;
    overflow: hidden;
    background: var(--backdrop);
  }
  .letterhead {
    position: absolute;
    left: 74px;
    top: 105px;
    width: 700px;
    height: 990px;
    background: var(--paper);
    box-shadow: 0 4px 18px rgba(0,0,0,0.18);
    overflow: hidden;
    font-family: "Arimo", Arial, sans-serif;
  }
  .side-band {
    position: absolute;
    top: 0;
    right: 0;
    width: 700px;
    height: 990px;
  }
  .brand {
    position: absolute;
    left: 34px;
    top: 48px;
    display: flex;
    align-items: center;
    gap: 10px;
  }
  .brand-dot {
    width: 26px;
    height: 26px;
    border-radius: 50%;
    background: var(--forest);
  }
  .brand-name {
    font-size: 27px;
    font-weight: 700;
    color: var(--forest);
    letter-spacing: 0.5px;
  }
  .contact {
    position: absolute;
    left: 270px;
    top: 22px;
    width: 340px;
    text-align: center;
    color: var(--ink);
    font-size: 15.5px;
    line-height: 19px;
  }
  .contact p { margin: 0; }
  .contact .address { text-align: left; margin-left: -4px; white-space: nowrap; }
  .header-rule {
    position: absolute;
    left: 18px;
    top: 128px;
    width: 586px;
    height: 2px;
    background: var(--forest);
  }
</style>
</head>
<body>
  <main class="letterhead">
    <svg class="side-band" viewBox="0 0 700 990" aria-hidden="true">
      <path d="M622 0 C632 120 642 260 636 360 C630 460 612 520 612 620 L612 990 L700 990 L700 0 Z" fill="var(--forest)"/>
    </svg>

    <div class="brand">
      <span class="brand-dot"></span>
      <span class="brand-name">Terra-Vantage</span>
    </div>

    <address class="contact">
      <p class="address">1180 Fernbrook Avenue. Maple Hollow,NJ 07000</p>
      <p>(555) 014 - 2290</p>
      <p>FAX: (555) 014 - 7735</p>
      <p>service@terra-vantage.example</p>
      <p>www.terra-vantage.example</p>
    </address>

    <div class="header-rule"></div>
  </main>
</body>
</html>
```